Business Goals Posters for display within company office and factory.

We have three (3) high level business goals we want to display in the office and factory areas of the business.

1. Under the heading of "QUALITY"
"We will have pride and ownership of every product and service delivered to our customers."

2. Under the heading of "PRODUCTIVITY"
"We will put the customer's expectations first and ensure our team is empowered to do so."

3. Under the heading of "SAFETY"
"We will shift our culture to ensure safety is our first thought on every job."

We would like a matching set of posters with these three headings and statements with a background suitable for display in a business environment. The posters will be displayed in sizes from A4 and A2.
The company's logo is Red and Black (see attachment) .
We make Electric and Hydraulic power packs for industrial market.
our website will give you an idea of what we do www.tarnwickdrives.com.au

Industry/Entity Type

Power Generation

Colors

Designer to choose colors to be used in the design.

Requirements
Must have
• The posters must use the exact text provided and have the headings listed.
• the three posters must have a common theme. they can be different in back ground but when side by side must look like a set.
• Be suitable for display as A4 and as A2.
Nice to have
• The text needs the be the star, the background needs to draw attention to the poster and the text with out over powering it,
Should not have
• not have photo's of generators or equipment as backgrounds

```html
<!DOCTYPE html>
<html lang="en">
<head>
<meta charset="utf-8">
<title>Tarnwick Drives – Productivity Goal Poster</title>
<link href="https://fonts.googleapis.com/css2?family=Saira+Extra+Condensed:wght@400;600&family=Yellowtail&display=swap" rel="stylesheet">
<style>
  :root {
    --paper-light: #ededeb;
    --paper-mid: #dcdcda;
    --paper-shade: #c4c4c2;
    --amber: #f0aa1c;
    --amber-deep: #e39b12;
    --ink: #1c1a17;
    --brand-red: #e3231f;
    --skin: #e2b49a;
    --skin-shadow: #c98f74;
  }
  html, body {
    margin: 0;
    padding: 0;
    overflow: hidden;
    background: var(--paper-light);
  }
  .poster {
    position: relative;
    width: 849px;
    height: 1200px;
    overflow: hidden;
  }
  .paper-backdrop {
    position: absolute;
    inset: 0;
    background: radial-gradient(ellipse at 35% 60%, var(--paper-light) 0%, var(--paper-mid) 70%, var(--paper-shade) 100%);
  }
  .torn-opening,
  .heading-underline {
    position: absolute;
    inset: 0;
  }
  .goal-statement {
    position: absolute;
    left: 395px;
    top: 276px;
    margin: 0;
    font-family: "Saira Extra Condensed", "Arial Narrow", sans-serif;
    font-stretch: condensed;
    font-weight: 400;
    font-size: 41px;
    line-height: 41px;
    letter-spacing: -0.3px;
    color: var(--ink);
  }
  .statement-line {
    display: block;
    white-space: nowrap;
  }
  .goal-heading {
    position: absolute;
    left: 285px;
    top: 985px;
    margin: 0;
    white-space: nowrap;
    font-family: "Yellowtail", cursive;
    font-weight: 400;
    font-size: 92px;
    line-height: 1;
    color: var(--ink);
    transform: rotate(-22deg);
    transform-origin: left bottom;
  }
  .writing-hand {
    position: absolute;
    left: 640px;
    top: 935px;
    width: 209px;
    height: 265px;
    background: linear-gradient(150deg, var(--skin) 0%, var(--skin-shadow) 100%);
    border-radius: 120px 0 0 0;
  }
  .brand-mark {
    position: absolute;
    left: 28px;
    top: 1118px;
    display: flex;
    align-items: center;
    gap: 10px;
  }
  .brand-square {
    width: 28px;
    height: 28px;
    background: var(--brand-red);
  }
  .brand-name {
    white-space: nowrap;
    font-family: "Saira Extra Condensed", "Arial Narrow", sans-serif;
    font-stretch: condensed;
    font-weight: 600;
    font-size: 28px;
    line-height: 1;
    color: var(--ink);
  }
</style>
</head>
<body>
  <main class="poster">
    <div class="paper-backdrop" role="img" aria-label="Light grey paper sheet with a torn, curled opening"></div>

    <svg class="torn-opening" width="849" height="1200" viewBox="0 0 849 1200" aria-hidden="true">
      <defs>
        <linearGradient id="amber-fill" x1="0" y1="0" x2="1" y2="1">
          <stop offset="0" stop-color="#f0aa1c"/>
          <stop offset="1" stop-color="#e39b12"/>
        </linearGradient>
      </defs>
      <polygon points="42,361 748,58 722,854" fill="url(#amber-fill)"/>
    </svg>

    <p class="goal-statement">
      <span class="statement-line">We will put the</span>
      <span class="statement-line">customer's</span>
      <span class="statement-line">expectations first</span>
      <span class="statement-line">and ensure our</span>
      <span class="statement-line">team is empowered</span>
      <span class="statement-line">to do so</span>
    </p>

    <svg class="heading-underline" width="849" height="1200" viewBox="0 0 849 1200" aria-hidden="true">
      <path d="M345 1098 C 450 1060, 550 1010, 625 975" fill="none" stroke="#1c1a17" stroke-width="4" stroke-linecap="round"/>
    </svg>
    <h1 class="goal-heading">Productivity</h1>

    <div class="writing-hand" role="img" aria-label="Hand holding a pen, writing the heading"></div>

    <div class="brand-mark">
      <span class="brand-square"></span>
      <span class="brand-name">Tarnwick Drives</span>
    </div>
  </main>
</body>
</html>
```